Web form face-lift for an online startup

We are a web startup building a SaaS application for the freight industry. The project is mainly dedicated to the paint the main form that our customer are using along the search results that the they get. All details are in the attached documents.
Updates
The application serves the Freight Forwarders community so please think towards this industry when using background images, banners, colors, icons, etc. Computer and technology images are irrelevant.
Customer fields at the top of the page is actually part of the form.
Target Market(s)
Usually business users (Sales people, procurement, shippers, freight forwarders). Some are less tech savvy and some appreciate the new trendy web apps.
Industry/Entity Type
Building
Colors
Designer to choose colors to be used in the design.
Look and feel
Each slider illustrates characteristics of the customer's brand and the style your logo design should communicate.

```html
<!DOCTYPE html>
<html lang="en">
<head>
<meta charset="utf-8">
<title>Cargoform DESK – Search for Quotes</title>
<link rel="stylesheet" href="https://fonts.googleapis.com/css2?family=Open+Sans:wght@400;600&family=Roboto:wght@400;500&display=swap">
<style>
:root{
  --red:#d10a0a;
  --dark:#23232f;
  --ink:#222;
  --grey:#e8e8e8;
  --grey-line:#d4d4d4;
  --footer:#140a08;
  --cyan:#12b5f0;
  --orange:#f47c20;
  --white:#fff;
}
*{box-sizing:border-box;margin:0;padding:0}
html,body{width:1200px;height:1127px;overflow:hidden}
body{position:relative;font-family:"Open Sans",Arial,sans-serif;font-size:13px;color:var(--ink);background:var(--white)}
.abs{position:absolute}

/* header */
.brand{left:118px;top:33px;font-family:"Roboto",Arial,sans-serif;font-size:34px;color:var(--red);letter-spacing:-.5px}
.util{top:14px;left:826px;display:flex;align-items:center;gap:22px;font-size:13px;color:#444}
.util .caret{display:inline-block;border:4px solid transparent;border-top-color:#333;margin-left:5px;vertical-align:-2px}
.user{display:flex;align-items:center;gap:6px;font-size:16px;color:#666}
.avatar{width:30px;height:30px;border-radius:50%;background:linear-gradient(#b9a79a,#6d5a4f)}
.nav{left:542px;top:64px;width:548px;height:46px;background:var(--red);display:flex;align-items:center}
.nav a{color:var(--white);text-decoration:none;font-size:13px;padding:0 9px;line-height:46px}
.nav a.home{background:var(--dark);font-weight:600;padding:0 14px}

/* hero */
.hero{left:0;top:110px;width:1200px;height:431px;background:linear-gradient(110deg,#120c06 0%,#1e150a 40%,#3f2d12 62%,#5a4a30 80%,#3b2c12 100%)}
.hero-title{left:137px;top:272px;font-size:19px;color:var(--white)}
.hero-input{left:135px;top:303px;width:384px;height:43px;background:var(--white);border-radius:2px;padding:0 8px;line-height:43px;font-size:13px}
.rate{left:141px;top:361px;color:var(--red);font-size:13px;display:flex;align-items:center;gap:4px}
.chk{width:11px;height:11px;border:1px solid #999;background:var(--white);display:inline-flex;align-items:center;justify-content:center}
.tabs{left:120px;top:501px;display:flex;gap:6px}
.tab{height:40px;background:#e4e4e4;display:flex;align-items:center;gap:6px;padding:0 8px;font-size:12.5px;border-radius:2px 2px 0 0;white-space:nowrap}
.tab.active{background:var(--white)}
.tab .pic{width:40px;height:40px;margin-top:-10px;flex:none}
.tab.more{background:var(--red);color:var(--white);padding:0 11px}

/* load table */
.thead{left:118px;top:567px;width:972px;height:39px;background:var(--dark);color:var(--white);font-weight:600;font-size:14px}
.thead span{position:absolute;top:11px}
.trow{left:118px;top:606px;width:972px;height:62px;background:#eee}
.field{position:absolute;height:28px;background:var(--white);border:1px solid var(--grey-line);text-align:center;line-height:26px;font-size:13px}
.unit{position:absolute;height:28px;display:flex}
.unit .lbl{background:var(--red);color:var(--white);font-size:15px;line-height:28px;width:50px;text-align:center}
.unit .drop{background:#111;width:31px;display:flex;align-items:center;justify-content:center}
.qty{left:15px;top:20px;width:40px;height:23px;background:#111;color:var(--white);text-align:center;line-height:23px;font-weight:600}
.select{left:212px;top:16px;width:211px;height:29px;background:#f3f3f3;border:1px solid #ddd;font-size:12px;line-height:27px;padding-left:9px}
.select .drop{position:absolute;right:0;top:-1px;width:34px;height:29px;background:var(--red);clip-path:polygon(20% 0,100% 0,100% 100%,20% 100%,0 50%);display:flex;align-items:center;justify-content:center;padding-left:6px}

.add{left:118px;top:685px;height:28px;display:flex;background:var(--dark);color:var(--white);font-size:14px}
.add .plus{width:36px;background:var(--red);font-size:22px;line-height:26px;text-align:center}
.add .txt{padding:0 17px 0 19px;line-height:28px}

.total{left:117px;top:729px;width:974px;height:44px;background:var(--grey)}
.total .word{position:absolute;left:579px;top:12px;font-size:14px}
.unit.dark .lbl{background:#111;width:43px}
.unit.dark .drop{background:var(--red);width:34px}

.route{top:795px;height:41px;background:#dedede;border:1px solid #ccc;display:flex;align-items:center;font-size:13.5px}
.route .tag{background:var(--red);color:var(--white);height:100%;line-height:39px;position:relative;margin-right:20px;padding-left:7px}
.route .tag::after{content:"";position:absolute;right:-7px;top:13px;border:7px solid transparent;border-left-color:var(--red);border-right:0}
.swap{left:578px;top:797px}

.options{left:117px;top:873px;width:974px;height:86px;background:var(--grey)}
.opt-title{left:16px;top:11px;width:101px;height:35px;background:#140a08;color:var(--white);font-size:16px;line-height:35px;text-align:center;letter-spacing:.3px}
.opts{position:absolute;top:57px;font-size:12.5px;display:flex;align-items:center;gap:4px}
.radio{width:11px;height:11px;border-radius:50%;border:1px solid #888;background:var(--white)}
.price{left:784px;top:24px;width:172px;height:28px;background:var(--white);border:1px solid var(--grey-line);font-size:12.5px;line-height:26px;padding-left:6px;color:#555}
.price .dd{position:absolute;right:4px;top:4px;width:17px;height:17px;border:1px solid #888;background:#eee;display:flex;align-items:center;justify-content:center}
.more-opt{position:absolute;right:18px;top:55px;font-size:12.5px;color:#555}

.btn{top:997px;height:44px;color:var(--white);font-size:15.5px;font-weight:500;font-family:"Roboto",Arial,sans-serif;text-align:center;line-height:42px;letter-spacing:.3px}
.btn.search{left:394px;width:174px;background:var(--cyan);border-bottom:3px solid #0a8fc2}
.btn.manual{left:621px;width:204px;background:var(--orange);border-bottom:3px solid #c85e10;line-height:38px}
.or{left:581px;top:1009px;font-size:16px}

.footer{left:0;top:1079px;width:1200px;height:48px;background:var(--footer);color:var(--white);font-size:12.5px}
.footer nav{position:absolute;top:16px;display:flex;gap:13px}
</style>
</head>
<body>

<div class="abs brand">Cargoform DESK</div>

<div class="abs util">
  <span><svg width="18" height="18" viewBox="0 0 18 18"><circle cx="9" cy="9" r="8" fill="none" stroke="#333" stroke-width="1.5"/><text x="9" y="13" text-anchor="middle" font-size="11" font-family="Arial" fill="#333">$</text></svg><i class="caret"></i></span>
  <span>English<i class="caret"></i></span>
  <span class="user"><span class="avatar" role="img" aria-label="User profile photo"></span>Martin Hale <i class="caret" style="border-top-color:#bbb"></i></span>
</div>

<nav class="abs nav">
  <a class="home" href="#">HOME</a><a href="#">Menu Item1</a><a href="#">Menu Item2</a><a href="#">Menu Item3</a><a href="#">Menu Item4</a><a href="#">Menu Item5</a>
</nav>

<div class="abs hero" role="img" aria-label="Photo of a freight truck with trailer driving on a highway at dusk"></div>

<div class="abs hero-title">Search for Quotes</div>
<div class="abs hero-input">Custome Name</div>
<div class="abs rate"><span class="chk"><svg width="9" height="9" viewBox="0 0 9 9"><path d="M1 4.5l2.5 2.5L8 1.5" stroke="#1a9a3a" stroke-width="1.6" fill="none"/></svg></span>Rate quote?</div>

<div class="abs tabs">
  <div class="tab active" style="width:142px"><span class="pic" role="img" aria-label="Wooden crate illustration" style="background:#c9a678"></span>Box or Pallet</div>
  <div class="tab" style="width:186px"><span class="pic" role="img" aria-label="Stacked shipping containers illustration" style="width:48px;background:#d9482b"></span>Shipping Container</div>
  <div class="tab" style="width:187px;padding:0 5px;gap:5px"><span class="pic" role="img" aria-label="Gift parcel illustration" style="width:34px;background:#a9dbf0"></span>Envelop or small Parcel</div>
  <div class="tab more" style="width:58px">MORE</div>
</div>

<div class="abs thead">
  <span style="left:20px">QTY</span><span style="left:88px">STACKABEL</span><span style="left:212px">LOAD</span>
  <span style="left:469px">LENGHT</span><span style="left:569px">WIDTH</span><span style="left:660px">HEIGHT</span><span style="left:816px">WEIGHT</span>
</div>
<div class="abs trow">
  <div class="abs qty">05</div>
  <span class="abs chk" style="left:121px;top:22px"></span>
  <div class="abs select">Box/Pallet<span class="drop"><svg width="10" height="10" viewBox="0 0 10 10"><path d="M1 1l4 4 4-4M1 5l4 4 4-4" stroke="#fff" stroke-width="1.6" fill="none"/></svg></span></div>
  <div class="field" style="left:469px;top:16px;width:59px">100</div>
  <div class="field" style="left:567px;top:16px;width:59px">100</div>
  <div class="field" style="left:658px;top:16px;width:59px">100</div>
  <div class="unit" style="left:720px;top:16px"><span class="lbl">cm</span><span class="drop"><svg width="10" height="10" viewBox="0 0 10 10"><path d="M1 1l4 4 4-4M1 5l4 4 4-4" stroke="#fff" stroke-width="1.6" fill="none"/></svg></span></div>
  <div class="field" style="left:813px;top:16px;width:59px">100</div>
  <div class="unit" style="left:875px;top:16px"><span class="lbl" style="width:46px">kg</span><span class="drop"><svg width="10" height="10" viewBox="0 0 10 10"><path d="M1 1l4 4 4-4M1 5l4 4 4-4" stroke="#fff" stroke-width="1.6" fill="none"/></svg></span></div>
</div>

<div class="abs add"><span class="plus">+</span><span class="txt" style="padding-right:23px">ADD MORE UNITS</span></div>

<div class="abs total">
  <span class="word">Total</span>
  <div class="field" style="left:625px;top:10px;width:59px">05</div>
  <div class="field" style="left:690px;top:10px;width:50px;text-align:left;padding-left:13px">01</div>
  <div class="unit dark" style="left:740px;top:10px"><span class="lbl">cm</span><span class="drop"><svg width="10" height="10" viewBox="0 0 10 10"><path d="M1 1l4 4 4-4M1 5l4 4 4-4" stroke="#fff" stroke-width="1.6" fill="none"/></svg></span></div>
  <div class="field" style="left:834px;top:10px;width:50px">100</div>
  <div class="unit dark" style="left:884px;top:10px"><span class="lbl" style="width:38px">kg</span><span class="drop"><svg width="10" height="10" viewBox="0 0 10 10"><path d="M1 1l4 4 4-4M1 5l4 4 4-4" stroke="#fff" stroke-width="1.6" fill="none"/></svg></span></div>
</div>

<div class="abs route" style="left:118px;width:397px"><span class="tag" style="width:56px">FROM</span>Shipping address or port</div>
<svg class="abs swap" width="28" height="36" viewBox="0 0 28 36"><path d="M3 11h21M17 4l7 7-7 7M25 25H4M11 18l-7 7 7 7" stroke="#111" stroke-width="3" fill="none"/></svg>
<div class="abs route" style="left:663px;width:428px"><span class="tag" style="width:45px;padding-left:13px">TO</span>Shipping address or port</div>

<div class="abs options">
  <div class="abs opt-title">OPTIONS</div>
  <div class="opts" style="left:19px"><span class="radio"></span>Import</div>
  <div class="opts" style="left:115px"><span class="radio"></span>Export</div>
  <div class="opts" style="left:215px">Incoterm: <b style="color:var(--red);font-weight:600">FCA</b></div>
  <div class="opts" style="left:407px"><span class="chk"><svg width="9" height="9" viewBox="0 0 9 9"><path d="M1 4.5l2.5 2.5L8 1.5" stroke="#1a9a3a" stroke-width="1.6" fill="none"/></svg></span><svg width="18" height="18" viewBox="0 0 18 18"><circle cx="9" cy="9" r="7.5" fill="none" stroke="#111" stroke-width="1.6"/><path d="M4 4l10 10" stroke="#111" stroke-width="1.6"/></svg></div>
  <div class="opts" style="left:466px"><span class="chk"></span><svg width="18" height="18" viewBox="0 0 18 18"><circle cx="9" cy="9" r="7.5" fill="none" stroke="#111" stroke-width="1.6"/><path d="M4 4l10 10" stroke="#111" stroke-width="1.6"/></svg></div>
  <div class="opts" style="left:523px"><span class="chk"></span><svg width="18" height="18" viewBox="0 0 18 18"><circle cx="9" cy="9" r="7.5" fill="none" stroke="#111" stroke-width="1.6"/><path d="M4 4l10 10M14 4L4 14" stroke="#111" stroke-width="1.6"/></svg></div>
  <div class="abs price">Price level<span class="dd"><svg width="9" height="6" viewBox="0 0 9 6"><path d="M1 1l3.5 3.5L8 1" stroke="#333" stroke-width="1.5" fill="none"/></svg></span></div>
  <span class="more-opt">More options</span>
</div>

<div class="abs btn search">SEARCH QUOTES</div>
<div class="abs or">OR</div>
<div class="abs btn manual">CREATIVITY MANUALLY</div>

<footer class="abs footer">
  <nav style="left:121px"><span>About us</span><span>Privacy policy</span><span>Terms of service</span><span>News</span></nav>
  <nav style="right:113px;gap:14px"><span>Blog</span><span>Friendbook</span><span>Chirper</span><span>WorkLink</span><span>ViewTube</span></nav>
</footer>

</body>
</html>
```